TIME BAR Design Project

DESIGN: TIME LAPSE BAR

We are looking for a fresh design for a time lapse bar which would appear on screen during an exercise video.

Please see a quick example attached. We would like it to be created in Photoshop or Illustrator, in layers. ( no after effects please).

We need a layer that would move to indicate the time passing.

We would like to manipulate the time as needed for various pieces.
Updates

Quick update:
please note the current bar in the sample picts was done in-house and is only intended to be a guide.  The bar does not have to resemble the sample. Thanks.

Target Market(s)

male /female 25-65 60% women.

Requirements
Must have
• Created in Photoshop or Illustrator.

Minimum 300DPI.

Please see that there is needs to be a place for the name of each exercise - this can appear and then fade out.
Nice to have
• -bar should match the mood of the set and colors.( see picts).

-bar CAN BE see-through so that the body's are seen behind it.
Should not have
• too high tech or masculine

too feminine

```html
<!DOCTYPE html>
<html lang="en">
<head>
<meta charset="utf-8">
<title>Time Lapse Bar</title>
<link rel="stylesheet" href="https://fonts.googleapis.com/css2?family=Varela+Round&display=swap">
<style>
  :root {
    --frame-dark: #141414;
    --frame-light: #f4f4f4;
    --board: #ffffff;
    --bar-top: #3d6d8d;
    --bar-bottom: #15374f;
    --bar-edge: #0c2638;
    --track: #ffffff;
    --progress-a: #b9d3a2;
    --progress-b: #a2c387;
    --play-red: #e3141b;
    --logo-ink: #98b3c5;
    --video-black: #050505;
    --studio-wall: #ece4d6;
    --studio-floor: #d99a55;
  }
  * { margin: 0; padding: 0; box-sizing: border-box; }
  html, body { width: 1200px; height: 900px; overflow: hidden; }
  body {
    position: relative;
    font-family: "Varela Round", sans-serif;
    background: linear-gradient(90deg, var(--frame-light) 0%, #8a8a8a 8%, var(--frame-dark) 22%, #d0d0d0 42%, var(--frame-light) 55%, var(--frame-dark) 70%, #9a9a9a 85%, var(--frame-light) 100%);
  }
  .board {
    position: absolute;
    left: 25px; top: 18px;
    width: 1150px; height: 864px;
    background: var(--board);
  }
  .time-bar { position: absolute; display: block; }
  .time-bar--large { left: 60px; top: 97px; width: 1048px; height: 68px; }
  .video-frame {
    position: absolute;
    left: 123px; top: 294px;
    width: 872px; height: 528px;
    background: var(--video-black);
  }
  .video-still {
    position: absolute;
    left: 2px; top: 11px;
    width: 868px; height: 490px;
    background: linear-gradient(180deg, var(--studio-wall) 0%, #efe7da 52%, #c9b59a 56%, var(--studio-floor) 62%, #e2aa68 100%);
  }
  .time-bar--overlay { left: 94px; top: 437px; width: 694px; height: 45px; opacity: 0.95; }
  .logo-text {
    font-family: "Varela Round", sans-serif;
    font-size: 28px;
    fill: var(--logo-ink);
  }
</style>
</head>
<body>
  <main class="board">
    <svg class="time-bar time-bar--large" viewBox="0 0 1048 68" aria-label="Exercise time progress bar">
      <defs>
        <linearGradient id="barBody" x1="0" y1="0" x2="0" y2="1">
          <stop offset="0" stop-color="var(--bar-top)"/>
          <stop offset="0.5" stop-color="#24506e"/>
          <stop offset="1" stop-color="var(--bar-bottom)"/>
        </linearGradient>
        <radialGradient id="playFace" cx="0.4" cy="0.35" r="0.7">
          <stop offset="0" stop-color="#ff5a4f"/>
          <stop offset="1" stop-color="var(--play-red)"/>
        </radialGradient>
        <pattern id="progressStripes" width="14" height="47" patternUnits="userSpaceOnUse">
          <rect width="14" height="47" fill="var(--progress-a)"/>
          <rect x="8" width="6" height="47" fill="var(--progress-b)"/>
        </pattern>
        <clipPath id="trackClip">
          <rect x="95" y="14" width="738" height="39" rx="19.5"/>
        </clipPath>
      </defs>
      <g class="bar-shell">
        <rect x="1.5" y="1.5" width="1045" height="65" rx="14" fill="url(#barBody)" stroke="var(--bar-edge)" stroke-width="3"/>
        <rect x="6" y="4" width="1036" height="6" rx="3" fill="#ffffff" opacity="0.18"/>
      </g>
      <g class="play-button">
        <circle cx="46" cy="34" r="22" fill="var(--bar-edge)"/>
        <circle cx="46" cy="34" r="17" fill="url(#playFace)" stroke="#ffffff" stroke-width="1.5"/>
        <path d="M40 24 L56 34 L40 44 Z" fill="#ffffff"/>
      </g>
      <g class="track">
        <rect x="91" y="10" width="746" height="47" rx="23.5" fill="var(--track)" stroke="#10324a" stroke-width="3"/>
        <rect class="track-progress" x="95" y="14" width="415" height="39" fill="url(#progressStripes)" clip-path="url(#trackClip)"/>
      </g>
      <text class="logo-text" x="948" y="43" text-anchor="middle">your logo</text>
    </svg>

    <section class="video-frame">
      <div class="video-still" role="img" aria-label="Exercise video still: instructors working out in a bright studio with wooden floor"></div>
      <svg class="time-bar time-bar--overlay" viewBox="0 0 1048 68" preserveAspectRatio="none" aria-label="Time progress bar shown over the video">
        <rect x="1.5" y="1.5" width="1045" height="65" rx="14" fill="url(#barBody)" stroke="var(--bar-edge)" stroke-width="3"/>
        <rect x="6" y="4" width="1036" height="6" rx="3" fill="#ffffff" opacity="0.18"/>
        <circle cx="46" cy="34" r="22" fill="var(--bar-edge)"/>
        <circle cx="46" cy="34" r="17" fill="url(#playFace)" stroke="#ffffff" stroke-width="1.5"/>
        <path d="M40 24 L56 34 L40 44 Z" fill="#ffffff"/>
        <rect x="91" y="10" width="746" height="47" rx="23.5" fill="var(--track)" stroke="#10324a" stroke-width="3"/>
        <rect x="95" y="14" width="373" height="39" fill="url(#progressStripes)" clip-path="url(#trackClip)"/>
        <text class="logo-text" x="948" y="43" text-anchor="middle">your logo</text>
      </svg>
    </section>
  </main>
</body>
</html>
```